Bref créative
Business card/letterhead/envelopes/fax cover sheet for plastic surgery practice
Morvan Plastic Surgery
Professional
Darek Olund, M.D.
unknown at this time
morvanaestheticclinic@mailbeam.example
www.darekolundmd.example
I would like name, address, phone number, fax number, and website included on front (no email address). I would also like the Continental Guild of Cosmetic Practice logo and Board Certified logo to appear on the front. The words "Plastic and Reconstructive Surgery, Hand Surgery, Cosmetic Surgery" should appear near or under my name.
The tagline "Results nobody can resist" should be included (front or back). Also, an area to write in the next appointment information should be on the back.
Continental Guild of Cosmetic Practitioners Logo
logo
Board Certification logo

```html
<!DOCTYPE html>
<html lang="en">
<head>
<meta charset="utf-8">
<title>Morvan Plastic Surgery – Stationery Set</title>
<link href="https://fonts.googleapis.com/css2?family=Montserrat:wght@600;700&family=Open+Sans:wght@400;600&display=swap" rel="stylesheet">
<style>
  :root {
    --navy: #1d2a86;
    --navy-deep: #101a5c;
    --blue-light: #4a63c9;
    --grey: #8c8f96;
    --grey-dark: #5b5e66;
    --paper: #ffffff;
    --stage: #f1f1f2;
    --ink: #3a3d44;
    --badge-teal: #7fb9c7;
    --badge-gold: #e5b64a;
  }
  * { margin: 0; padding: 0; box-sizing: border-box; }
  html, body { width: 1200px; height: 446px; overflow: hidden; }
  body {
    background: linear-gradient(180deg, #ffffff 0%, var(--stage) 100%);
    font-family: "Open Sans", sans-serif;
    color: var(--ink);
    position: relative;
  }
  .piece { position: absolute; background: var(--paper); box-shadow: 0 1px 3px rgba(0,0,0,.25); overflow: hidden; }
  .label { position: absolute; font-size: 5px; color: var(--grey-dark); text-align: center; }
  .brand { font-family: "Montserrat", sans-serif; font-weight: 700; color: var(--navy); letter-spacing: .5px; display: flex; align-items: center; gap: 3px; }
  .brand-dot { border-radius: 50%; background: var(--navy); display: inline-block; }
  .brand-sub { font-size: 3.2px; color: var(--grey); letter-spacing: .3px; }
  .tiny { font-size: 3.4px; line-height: 1.35; }
  .badge { position: absolute; border-radius: 50%; }
  .badge-guild { border: 1.5px solid var(--badge-teal); }
  .badge-board { background: radial-gradient(circle, var(--badge-gold) 35%, #f4dca0 70%); }

  /* business cards */
  .card { left: 12px; width: 106px; height: 63px; }
  .card-front { top: 98px; }
  .card-front .brand { position: absolute; left: 7px; top: 10px; font-size: 11px; }
  .card-front .brand-sub { position: absolute; left: 7px; top: 24px; }
  .card-front .wave { position: absolute; right: 0; top: 0; width: 62px; height: 63px; }
  .card-front .details { position: absolute; right: 5px; top: 8px; width: 40px; color: #fff; text-align: right; }
  .card-front .name { font-size: 4.2px; font-weight: 600; }
  .card-back { padding: 6px 7px; }
  .card-back-1 { top: 186px; }
  .card-back-2 { top: 266px; background: linear-gradient(180deg, #fff, #e9e9ec); }
  .appt-title { font-size: 5px; font-weight: 600; color: var(--navy); text-align: center; margin-bottom: 4px; }
  .appt-row { display: flex; align-items: flex-end; gap: 2px; font-size: 3.6px; margin-bottom: 5px; width: 54px; }
  .appt-row span.line { flex: 1; border-bottom: .5px solid var(--grey); }
  .card-back .tagline { position: absolute; left: 7px; bottom: 5px; font-size: 3.4px; color: var(--navy); font-style: italic; }

  /* letterheads */
  .letterhead { top: 19px; width: 214px; height: 307px; }
  .letterhead-1 { left: 164px; }
  .letterhead-2 { left: 399px; }
  .letterhead .brand { position: absolute; left: 16px; top: 16px; font-size: 14px; }
  .letterhead .brand-sub { position: absolute; left: 16px; top: 34px; }
  .letterhead .contact { position: absolute; right: 14px; top: 16px; width: 58px; color: var(--grey-dark); }
  .letterhead .band { position: absolute; left: 0; bottom: 0; width: 214px; height: 32px; }
  .letterhead .footer-text { position: absolute; left: 0; right: 0; bottom: 5px; text-align: center; color: #fff; font-size: 3.2px; }
  .letterhead .badge-guild { right: 44px; bottom: 36px; width: 20px; height: 20px; }
  .letterhead .badge-board { right: 16px; bottom: 38px; width: 18px; height: 18px; }

  /* envelopes */
  .envelope { left: 636px; width: 192px; }
  .env-back-blue { top: 48px; height: 84px; background: linear-gradient(180deg, var(--navy-deep), var(--blue-light) 55%, var(--navy)); }
  .env-back-grey { top: 134px; height: 82px; background: linear-gradient(180deg, #6e7078, #d8d9dc 55%, #85878e); }
  .env-front-band { top: 228px; height: 72px; }
  .env-front-logo { top: 306px; height: 78px; }
  .envelope .flap { position: absolute; inset: 0; width: 100%; height: 100%; }
  .envelope .seal { position: absolute; left: 50%; top: 40px; transform: translateX(-50%); width: 8px; height: 8px; border-radius: 50%; background: rgba(255,255,255,.7); }
  .env-front-band .band { position: absolute; left: 0; bottom: 0; width: 192px; height: 22px; }
  .env-front-band .return { position: absolute; left: 50%; top: 28px; transform: translateX(-50%); display: flex; align-items: center; gap: 5px; }
  .env-front-band .brand { font-size: 7px; }
  .env-front-logo .brand { position: absolute; left: 8px; top: 8px; font-size: 11px; }
  .env-front-logo .return { position: absolute; left: 8px; top: 22px; color: var(--grey-dark); }
  .env-front-logo .band { position: absolute; left: 0; bottom: 0; width: 192px; height: 12px; }
</style>
</head>
<body>

  <!-- Business card front -->
  <div class="piece card card-front">
    <div class="brand"><span class="brand-dot" style="width:4px;height:4px"></span>MORVAN</div>
    <div class="brand-sub">Morvan Plastic Surgery</div>
    <svg class="wave" viewBox="0 0 62 63" preserveAspectRatio="none" aria-hidden="true">
      <defs><linearGradient id="cardBlue" x1="0" y1="0" x2="1" y2="1"><stop offset="0" stop-color="#4a63c9"/><stop offset="1" stop-color="#101a5c"/></linearGradient></defs>
      <path d="M18 0 H62 V63 H6 C22 44 4 20 18 0 Z" fill="url(#cardBlue)"/>
      <path d="M14 0 C2 20 18 44 2 63" fill="none" stroke="#c9cfe8" stroke-width=".8"/>
    </svg>
    <div class="details tiny">
      <div class="name">Darek Olund, M.D.</div>
      <div>Plastic and Reconstructive Surgery, Hand Surgery, Cosmetic Surgery</div>
      <div style="margin-top:3px">214 Harbor Lane, Fairview</div>
      <div>Tel 555 014 2290</div>
      <div>Fax 555 014 2291</div>
      <div>www.darekolundmd.example</div>
    </div>
  </div>
  <div class="label" style="left:12px;top:163px;width:106px">Business Card Front</div>

  <!-- Business card back 1 -->
  <div class="piece card card-back card-back-1">
    <div class="appt-title">Next Appointment</div>
    <div class="appt-row">Day <span class="line"></span></div>
    <div class="appt-row">Date <span class="line"></span></div>
    <div class="appt-row">Time <span class="line"></span></div>
    <div class="badge badge-guild" style="right:20px;top:22px;width:12px;height:12px"></div>
    <div class="badge badge-board" style="right:6px;top:22px;width:11px;height:11px"></div>
    <div class="tagline">Results nobody can resist</div>
  </div>
  <div class="label" style="left:12px;top:251px;width:106px">Card Back Option 1</div>

  <!-- Business card back 2 -->
  <div class="piece card card-back card-back-2">
    <div class="appt-title">Next Appointment</div>
    <div class="appt-row">Day <span class="line"></span></div>
    <div class="appt-row">Date <span class="line"></span></div>
    <div class="appt-row">Time <span class="line"></span></div>
    <div class="badge badge-guild" style="right:20px;top:22px;width:12px;height:12px"></div>
    <div class="badge badge-board" style="right:6px;top:22px;width:11px;height:11px"></div>
    <div class="tagline">Results nobody can resist</div>
  </div>
  <div class="label" style="left:12px;top:331px;width:106px">Card Back Option 2</div>

  <!-- Letterhead 1 -->
  <div class="piece letterhead letterhead-1">
    <div class="brand"><span class="brand-dot" style="width:5px;height:5px"></span>MORVAN</div>
    <div class="brand-sub">Morvan Plastic Surgery</div>
    <div class="contact tiny">
      <div>214 Harbor Lane, Fairview</div>
      <div>Tel 555 014 2290</div>
      <div>Fax 555 014 2291</div>
      <div>www.darekolundmd.example</div>
    </div>
    <div class="badge badge-guild"></div>
    <div class="badge badge-board"></div>
    <svg class="band" viewBox="0 0 214 32" preserveAspectRatio="none" aria-hidden="true">
      <path d="M0 14 C70 2 140 26 214 10 V32 H0 Z" fill="#1d2a86"/>
      <path d="M0 12 C70 0 140 24 214 8" fill="none" stroke="#9aa6d8" stroke-width=".7"/>
    </svg>
    <div class="footer-text">214 Harbor Lane, Fairview · Tel 555 014 2290 · www.darekolundmd.example</div>
  </div>
  <div class="label" style="left:164px;top:332px;width:214px">Letterhead Option 1</div>

  <!-- Letterhead 2 -->
  <div class="piece letterhead letterhead-2">
    <div class="brand"><span class="brand-dot" style="width:5px;height:5px"></span>MORVAN</div>
    <div class="brand-sub">Morvan Plastic Surgery</div>
    <div class="contact tiny">
      <div>214 Harbor Lane, Fairview</div>
      <div>Tel 555 014 2290</div>
      <div>Fax 555 014 2291</div>
      <div>www.darekolundmd.example</div>
    </div>
    <div class="badge badge-guild"></div>
    <div class="badge badge-board"></div>
    <svg class="band" viewBox="0 0 214 32" preserveAspectRatio="none" aria-hidden="true">
      <path d="M0 20 C60 12 150 16 214 6 V32 H0 Z" fill="#101a5c"/>
      <path d="M0 18 C60 10 150 14 214 4" fill="none" stroke="#9aa6d8" stroke-width=".7"/>
    </svg>
    <div class="footer-text">214 Harbor Lane, Fairview · Tel 555 014 2290 · www.darekolundmd.example</div>
  </div>
  <div class="label" style="left:399px;top:332px;width:214px">Letterhead Option 2</div>

  <!-- Envelope back, blue -->
  <div class="piece envelope env-back-blue">
    <svg class="flap" viewBox="0 0 192 84" preserveAspectRatio="none" aria-hidden="true">
      <path d="M0 0 L96 48 L192 0" fill="none" stroke="rgba(255,255,255,.45)" stroke-width=".8"/>
      <path d="M0 84 L80 40 M192 84 L112 40" fill="none" stroke="rgba(255,255,255,.25)" stroke-width=".6"/>
    </svg>
    <div class="seal"></div>
  </div>

  <!-- Envelope back, grey -->
  <div class="piece envelope env-back-grey">
    <svg class="flap" viewBox="0 0 192 82" preserveAspectRatio="none" aria-hidden="true">
      <path d="M0 0 L96 46 L192 0" fill="none" stroke="rgba(255,255,255,.6)" stroke-width=".8"/>
      <path d="M0 82 L80 38 M192 82 L112 38" fill="none" stroke="rgba(255,255,255,.35)" stroke-width=".6"/>
    </svg>
    <div class="seal" style="top:38px"></div>
  </div>

  <!-- Envelope front with band -->
  <div class="piece envelope env-front-band">
    <div class="return">
      <div class="brand"><span class="brand-dot" style="width:3px;height:3px"></span>MORVAN</div>
      <div class="tiny" style="color:var(--grey-dark)">214 Harbor Lane, Fairview</div>
    </div>
    <svg class="band" viewBox="0 0 192 22" preserveAspectRatio="none" aria-hidden="true">
      <path d="M0 12 C64 2 128 20 192 6 V22 H0 Z" fill="#1d2a86"/>
    </svg>
  </div>

  <!-- Envelope front with logo -->
  <div class="piece envelope env-front-logo">
    <div class="brand"><span class="brand-dot" style="width:4px;height:4px"></span>MORVAN</div>
    <div class="return tiny">
      <div>Morvan Plastic Surgery</div>
      <div>214 Harbor Lane, Fairview</div>
    </div>
    <svg class="band" viewBox="0 0 192 12" preserveAspectRatio="none" aria-hidden="true">
      <path d="M0 6 C64 0 128 10 192 2 V12 H0 Z" fill="#1d2a86"/>
    </svg>
  </div>
  <div class="label" style="left:636px;top:389px;width:192px">Envelope Front/Back</div>

</body>
</html>
```